Page Design For Free Videos Download Page

We have page that already has functional code here http://www.vexarnoble.com/
The project is to create a better design and layout of that page.

You may use the password "1234" to access the features when prompted.*** Please note that the existing design is just a draft for your reference.

The page you design should have seven main components as described below:

1. Header. Include our logo and the title "Free FlickerSpans Updated Monthly"

2. Navigation. This is not yet implemented but we would like you to have these choices:

Free Videos
FlickerSpans
PebbleClips
Free Sign-Up
About Us

3. The main background image or pattern. You may incorporate our logo in some way in this background if you like (abstract, tiling, etc) but this is not required.

4. Preview Images. You can see that there are a few groups showing recent months of the free videos we will offer for download on this page. We prefer to keep the current size and functionality of the images as-is.

There will always be 16 images in rows of 4 for a clean layout. You can see from the page how these will look in rows of 4. The images will be the same size and function as the images in the example page.

5. Row text. Each row has some text showing what month the free videos belong to. The text can be displayed in any way you see fit. In the example page it is simply above each row of images but you can resize and move the text anywhere you feel is best for the design.

6. Password pop-up. If a user has not entered the password and attempts to download a video by clicking on an image, a pop-up appears asking for the password. This is only partially implemented on the test page. We want to give the user two options:

a. Please enter your password.
-or-
b. Immediately receive the password by entering your email address.

For "b" also include a checkbox: "Send me monthly updates when new free downloads become available."
also allow the user to enter their email here a

7. Banner Area. Below the image groups will be banners where we will advertise products on our website www.flickerspans.com. This is the main reason for creating this page - drive traffic to this page and then get them to sign-up to receive the password and eventually click on a banner to browse our website.

For this part you should design 4 wide template banners stacked one on top of another - each with a different layout and style but still keeping with the general theme of the page (no Flash please).

If we select you, we will give you assets (images and text) to insert into your 4 banner templates for the final files delivery. This way for now the banners can be generic.

Target Market(s)

Video professionals in the editing and live performance markets.

Industry/Entity Type

Delivery

Requirements
Must have
• 4 rows of 4 images the same size as in the example page. The image spacing and layout can change to fit your design however.

```html
<!DOCTYPE html>
<html lang="en">
<head>
<meta charset="utf-8">
<title>Free FlickerSpans</title>
<link rel="stylesheet" href="https://fonts.googleapis.com/css2?family=Titillium+Web:wght@300;400;600&family=Arimo:wght@400;700&display=swap">
<style>
:root{
  --page:#58626f;
  --panel:#44525f;
  --panel-light:#4d5b68;
  --panel-deep:#3c4955;
  --nav:#3f4c5a;
  --ink-dark:#3a4756;
  --ink-soft:#7a8794;
  --rule:#4a5562;
  --popup:#3d4a58;
  --popup-edge:#56636f;
  --white:#ffffff;
  --accent:#4aa3e8;
  --link:#6fb2e4;
}
*{box-sizing:border-box;margin:0;padding:0}
html,body{width:1200px;height:2844px;overflow:hidden}
body{background:var(--page);font-family:"Titillium Web",sans-serif;position:relative}
.abs{position:absolute}
.brand-wrap{left:0;width:1200px;top:38px}
.brand-dot{display:block;width:72px;height:72px;border-radius:50%;background:var(--ink-dark);margin:0 auto}
.brand{left:0;width:1200px;top:118px;text-align:center;font-size:62px;font-weight:300;color:var(--ink-dark);line-height:1;letter-spacing:1px}
.tagline{left:0;width:1200px;top:192px;text-align:center;font-size:20px;font-weight:600;color:var(--ink-dark);letter-spacing:.5px;line-height:1.2}
.nav{left:108px;top:243px;width:982px;height:75px;background:var(--nav)}
.nav-item{position:absolute;top:0;line-height:75px;font-size:23px;font-weight:600;color:var(--ink-soft);transform:translateX(-50%);white-space:nowrap}
.nav-signin{font-weight:400}
.nav-caret{position:absolute;left:934px;top:33px}
.page-title{left:0;width:1200px;top:326px;text-align:center;font-size:64px;font-weight:300;color:var(--ink-dark);line-height:1.2}
.rule{left:108px;width:982px;height:2px;background:var(--rule)}
.rule-title{background:#3a4551}
.month{left:0;width:1200px;text-align:center;font-size:40px;font-weight:300;color:var(--ink-dark);line-height:1}
.tile{width:222px;height:205px;background:var(--panel)}
.tile svg{position:absolute;right:14px;bottom:14px}
.archive{left:0;width:1200px;top:1713px;text-align:center;font-size:28px;font-weight:300;color:var(--ink-dark)}
.ad-label{left:0;width:1200px;top:1802px;text-align:center;font-size:18px;font-weight:300;color:var(--ink-dark)}
.banner{left:110px;width:982px;height:148px;background:var(--panel);overflow:hidden}
.banner-block{position:absolute;background:var(--panel-light)}
.banner-bar{position:absolute;height:14px;background:var(--panel-deep)}
.banner-button{position:absolute;width:150px;height:40px;background:var(--panel-deep)}
.footer{left:0;width:1200px;top:2614px;text-align:center;font-size:19px;font-weight:300;color:var(--ink-dark)}
.footer-mark{left:0;width:1200px;top:2664px;text-align:center;font-size:18px;font-weight:600;color:var(--ink-dark)}
.popup{left:771px;top:318px;width:320px;height:520px;background:var(--popup);border:2px solid var(--popup-edge);border-top:none;font-family:"Arimo",sans-serif;color:var(--white)}
.popup-brand{position:absolute;left:22px;top:14px;font-family:"Titillium Web",sans-serif;font-size:30px;font-weight:400;color:var(--white);line-height:1}
.popup-label{position:absolute;left:23px;font-size:15px;font-weight:700}
.popup-input{position:absolute;left:23px;width:273px;height:30px;background:var(--white)}
.popup-check{position:absolute;left:27px;width:18px;height:18px;background:var(--white)}
.popup-small{position:absolute;left:56px;font-size:13px;line-height:1.2}
.popup-button{position:absolute;width:106px;height:38px;background:var(--accent);font-family:"Titillium Web",sans-serif;font-weight:600;font-size:20px;line-height:38px;text-align:center}
.popup-forgot{position:absolute;left:29px;top:264px;font-size:12.5px;color:var(--link)}
.popup-rule{position:absolute;left:23px;top:296px;width:273px;height:2px;background:#a9b3bd}
.popup-note{position:absolute;left:23px;top:312px;width:275px;font-size:12px;line-height:1.2;color:#e6ebef}
</style>
</head>
<body>

<header>
  <div class="abs brand-wrap"><span class="brand-dot"></span></div>
  <div class="abs brand">flickerspans</div>
  <div class="abs tagline">FREE FLICKERSPANS UPDATED MONTHLY</div>
</header>

<nav class="abs nav">
  <span class="nav-item" style="left:92px">Free Videos</span>
  <span class="nav-item" style="left:250px">FlickerSpans</span>
  <span class="nav-item" style="left:404px">PebbleClips</span>
  <span class="nav-item" style="left:558px">Free Sign-Up</span>
  <span class="nav-item" style="left:704px">About Us</span>
  <span class="nav-item nav-signin" style="left:870px">Sign In</span>
  <svg class="nav-caret" width="14" height="10" viewBox="0 0 14 10"><path d="M0 0h14L7 10z" fill="#7a8794"/></svg>
</nav>

<h1 class="abs page-title">Free FlickerSpans</h1>
<div class="abs rule rule-title" style="top:422px"></div>

<main>
  <h2 class="abs month" style="top:439px">APRIL 2013</h2>
  <div class="abs tile" style="left:110px;top:495px"><svg width="30" height="30" viewBox="0 0 30 30"><path d="M3 16v11h24V16h-4v7H7v-7z M12 3h6v9h5l-8 8-8-8h5z" fill="#5e6a77"/></svg></div>
  <div class="abs tile" style="left:364px;top:495px"><svg width="34" height="34" viewBox="0 0 34 34"><path d="M32 2 18 8 8 20l6 6 12-10z M8 20l-6 2 3 3z M14 26l-2 6 3-3z M6 24l4 4-7 5z" fill="#5e6a77"/></svg></div>
  <div class="abs tile" style="left:616px;top:495px"></div>
  <div class="abs tile" style="left:868px;top:495px"></div>
  <div class="abs rule" style="top:741px"></div>

  <h2 class="abs month" style="top:759px">MARCH 2013</h2>
  <div class="abs tile" style="left:110px;top:811px"><svg width="30" height="30" viewBox="0 0 30 30"><path d="M3 16v11h24V16h-4v7H7v-7z M12 3h6v9h5l-8 8-8-8h5z" fill="#5e6a77"/></svg></div>
  <div class="abs tile" style="left:364px;top:811px"><svg width="30" height="30" viewBox="0 0 30 30"><path d="M3 16v11h24V16h-4v7H7v-7z M12 3h6v9h5l-8 8-8-8h5z" fill="#5e6a77"/></svg></div>
  <div class="abs tile" style="left:616px;top:811px"><svg width="34" height="34" viewBox="0 0 34 34"><path d="M32 2 18 8 8 20l6 6 12-10z M8 20l-6 2 3 3z M14 26l-2 6 3-3z M6 24l4 4-7 5z" fill="#5e6a77"/></svg></div>
  <div class="abs tile" style="left:868px;top:811px"><svg width="30" height="30" viewBox="0 0 30 30"><path d="M3 16v11h24V16h-4v7H7v-7z M12 3h6v9h5l-8 8-8-8h5z" fill="#5e6a77"/></svg></div>
  <div class="abs rule" style="top:1058px"></div>

  <h2 class="abs month" style="top:1076px">FEBRUARY 2013</h2>
  <div class="abs tile" style="left:110px;top:1128px"></div>
  <div class="abs tile" style="left:364px;top:1128px"></div>
  <div class="abs tile" style="left:616px;top:1128px"></div>
  <div class="abs tile" style="left:868px;top:1128px"></div>
  <div class="abs rule" style="top:1376px"></div>

  <h2 class="abs month" style="top:1394px">JANUARY 2013</h2>
  <div class="abs tile" style="left:110px;top:1446px"></div>
  <div class="abs tile" style="left:364px;top:1446px"></div>
  <div class="abs tile" style="left:616px;top:1446px"></div>
  <div class="abs tile" style="left:868px;top:1446px"></div>
  <div class="abs rule" style="top:1693px"></div>

  <p class="abs archive">view archive &lt; older posts &gt;</p>
  <div class="abs rule" style="top:1776px"></div>
</main>

<section>
  <p class="abs ad-label">&lt;Advertisement area&gt;</p>

  <div class="abs banner banner-media-left" style="top:1852px">
    <div class="banner-block" style="left:0;top:0;width:300px;height:148px" role="img" aria-label="Product image area"></div>
    <div class="banner-bar" style="left:340px;top:42px;width:380px;height:20px"></div>
    <div class="banner-bar" style="left:340px;top:80px;width:300px"></div>
    <div class="banner-button" style="left:790px;top:54px"></div>
  </div>

  <div class="abs banner banner-media-right" style="top:2032px">
    <div class="banner-bar" style="left:40px;top:40px;width:420px;height:20px"></div>
    <div class="banner-bar" style="left:40px;top:78px;width:340px"></div>
    <div class="banner-bar" style="left:40px;top:104px;width:260px"></div>
    <div class="banner-block" style="left:600px;top:0;width:382px;height:148px" role="img" aria-label="Product image area"></div>
  </div>

  <div class="abs banner banner-strip" style="top:2212px">
    <div class="banner-block" style="left:40px;top:24px;width:160px;height:100px" role="img" aria-label="Product image area"></div>
    <div class="banner-block" style="left:220px;top:24px;width:160px;height:100px" role="img" aria-label="Product image area"></div>
    <div class="banner-block" style="left:400px;top:24px;width:160px;height:100px" role="img" aria-label="Product image area"></div>
    <div class="banner-bar" style="left:600px;top:48px;width:320px;height:20px"></div>
    <div class="banner-button" style="left:600px;top:84px"></div>
  </div>

  <div class="abs banner banner-centered" style="top:2392px">
    <div class="banner-block" style="left:0;top:0;width:982px;height:148px;background:linear-gradient(90deg,#44525f,#4d5b68 50%,#44525f)" role="img" aria-label="Wide product background"></div>
    <div class="banner-bar" style="left:291px;top:44px;width:400px;height:20px"></div>
    <div class="banner-button" style="left:416px;top:80px"></div>
  </div>
</section>

<footer>
  <p class="abs footer">Copyright &nbsp;|&nbsp; About Us</p>
  <p class="abs footer-mark">flickerspans</p>
</footer>

<aside class="abs popup">
  <div class="popup-brand">flickerspans</div>
  <span class="popup-label" style="top:70px">Email:</span>
  <span class="popup-input" style="top:95px"></span>
  <span class="popup-label" style="top:146px">Password:</span>
  <span class="popup-input" style="top:171px"></span>
  <span class="popup-check" style="top:228px"></span>
  <span class="popup-small" style="top:229px">Remember Me</span>
  <span class="popup-button" style="left:190px;top:220px">Sign In</span>
  <span class="popup-forgot">Forgot Password?</span>
  <span class="popup-rule"></span>
  <p class="popup-note">Immediately receive the password by entering your email address.</p>
  <span class="popup-label" style="top:354px">Email:</span>
  <span class="popup-input" style="top:378px"></span>
  <span class="popup-check" style="top:424px"></span>
  <span class="popup-small" style="top:423px;width:240px;font-size:12px">Send me monthly updates when new free downloads become available.</span>
  <span class="popup-button" style="left:190px;top:466px">Send</span>
</aside>

</body>
</html>
```